TLR Property - Business Cards

Looking for a business card & general letterhead, signage etc design for our new logo.

Colours:
000a20
0056a2
00b5ef
0088ce
68cef2

Fonts:
Poppins
Karla

Please keep look and feel of new brand - example in the zip package I sent.

```html
<!DOCTYPE html>
<html lang="en">
<head>
<meta charset="utf-8">
<title>TLR Property – Stationery</title>
<link rel="stylesheet" href="https://fonts.googleapis.com/css2?family=Poppins:wght@500;600;700&family=Montserrat:wght@400;500&family=Karla:wght@400;500&display=swap">
<style>
  :root {
    --navy: #000a20;
    --card-dark: #1e2133;
    --blue: #0056a2;
    --sky: #00b5ef;
    --mid: #0088ce;
    --pale: #68cef2;
    --paper: #ffffff;
    --ink: #3a3a3a;
    --muted: #8e8e8e;
    --rule: #cfcfcf;
    --backdrop: #b4b4b4;
  }
  * { box-sizing: border-box; margin: 0; padding: 0; }
  html, body { width: 1200px; height: 1068px; overflow: hidden; background: var(--backdrop); }
  .canvas { position: relative; width: 1200px; height: 1068px; }
  .icon { width: 11px; height: 11px; display: inline-block; vertical-align: middle; }

  /* Letterhead */
  .letterhead { position: absolute; left: 204px; top: 108px; width: 602px; height: 852px; background: var(--paper); box-shadow: 0 6px 24px rgba(0,0,0,.18); }
  .brand { position: absolute; display: flex; align-items: center; gap: 8px; font-family: "Poppins", sans-serif; font-weight: 600; white-space: nowrap; }
  .brand-dot { border-radius: 50%; background: var(--sky); }
  .letterhead .brand { left: 43px; top: 76px; font-size: 30px; color: var(--blue); }
  .letterhead .brand-dot { width: 18px; height: 18px; }
  .head-contact { position: absolute; right: 41px; top: 48px; text-align: right; font-family: "Karla", sans-serif; font-size: 8.6px; color: #555; line-height: 1.05; }
  .head-contact li { list-style: none; display: flex; justify-content: flex-end; align-items: center; gap: 4px; margin-bottom: 7px; }
  .head-contact li.addr { margin-bottom: 14px; }
  .head-rule { position: absolute; left: 43px; top: 153px; width: 515px; height: 1px; background: var(--rule); }
  .recipient { position: absolute; left: 43px; top: 218px; font-family: "Montserrat", sans-serif; font-size: 11px; color: var(--ink); line-height: 1.1; }
  .recipient h2 { font-family: "Poppins", sans-serif; font-weight: 600; font-size: 16.5px; color: var(--blue); margin-bottom: 7px; letter-spacing: .2px; }
  .recipient p { margin-bottom: 7px; }
  .recipient p.tight { margin-bottom: 0; }
  .body-copy { position: absolute; left: 44px; top: 338px; width: 515px; font-family: "Montserrat", sans-serif; font-size: 12px; line-height: 18.7px; color: var(--muted); text-align: justify; }
  .body-copy p + p { margin-top: 18.7px; }
  .signature { position: absolute; left: 69px; top: 611px; width: 86px; height: 56px; background: linear-gradient(90deg, #f1f1f1, #e6e6e6); }
  .signer { position: absolute; left: 44px; top: 676px; font-family: "Poppins", sans-serif; font-weight: 600; font-size: 16.5px; color: #111; }
  .foot-band { position: absolute; left: 0; top: 785px; width: 385px; height: 28px; background: var(--blue); clip-path: polygon(0 0, 366px 0, 385px 28px, 0 28px); display: flex; align-items: center; padding-left: 45px; gap: 6px; font-family: "Montserrat", sans-serif; font-weight: 500; font-size: 8.4px; letter-spacing: 2px; color: #fff; }

  /* Business card – front */
  .card { position: absolute; width: 296px; height: 182px; box-shadow: 0 8px 22px rgba(0,0,0,.28); overflow: hidden; }
  .card-front { left: 653px; top: 283px; background: var(--paper); width: 294px; }
  .card-front h3 { position: absolute; left: 21px; top: 20px; font-family: "Poppins", sans-serif; font-weight: 500; font-size: 13px; color: var(--sky); white-space: nowrap; }
  .card-front h3 strong { font-weight: 700; color: var(--blue); }
  .card-front .role { position: absolute; left: 21px; top: 37px; font-family: "Karla", sans-serif; font-size: 8.5px; color: #666; }
  .card-addr { position: absolute; left: 21px; top: 95px; display: flex; gap: 3px; font-family: "Karla", sans-serif; font-size: 6.4px; line-height: 1.3; color: #666; }
  .card-addr .icon { width: 8px; height: 8px; margin-top: 1px; }
  .card-band { position: absolute; left: 0; top: 116px; width: 157px; height: 43px; background: var(--blue); clip-path: polygon(0 0, 138px 0, 157px 43px, 0 43px); padding: 4px 0 0 21px; font-family: "Karla", sans-serif; font-size: 6.6px; color: #fff; }
  .card-band li { list-style: none; display: flex; align-items: center; gap: 3px; height: 13.5px; }
  .card-band .icon { width: 8px; height: 8px; }

  /* Business card – back */
  .card-back { left: 652px; top: 494px; width: 299px; background: var(--card-dark); display: flex; align-items: center; justify-content: center; }
  .card-back .brand { position: static; font-size: 30px; color: #fff; }
  .card-back .brand-dot { width: 18px; height: 18px; }
</style>
</head>
<body>
<svg width="0" height="0" style="position:absolute" aria-hidden="true">
  <defs>
    <symbol id="ic-pin" viewBox="0 0 12 12"><rect width="12" height="12" rx="1.5" fill="#0056a2"/><path d="M6 2.2a2.6 2.6 0 0 0-2.6 2.6C3.4 6.8 6 9.8 6 9.8s2.6-3 2.6-5A2.6 2.6 0 0 0 6 2.2z" fill="#fff"/><circle cx="6" cy="4.8" r="1" fill="#0056a2"/></symbol>
    <symbol id="ic-phone" viewBox="0 0 12 12"><rect width="12" height="12" rx="1.5" fill="#00b5ef"/><path d="M3.3 2.5l1.5-.2.8 1.9-1 .8a5 5 0 0 0 2.4 2.4l.8-1 1.9.8-.2 1.5c-3.4.3-6.5-2.8-6.2-6.2z" fill="#fff"/></symbol>
    <symbol id="ic-mail" viewBox="0 0 12 12"><rect width="12" height="12" rx="1.5" fill="#00b5ef"/><rect x="2.3" y="3.5" width="7.4" height="5" fill="#fff"/><path d="M2.3 3.6L6 6.5l3.7-2.9" stroke="#00b5ef" stroke-width=".8" fill="none"/></symbol>
    <symbol id="ic-web" viewBox="0 0 12 12"><rect width="12" height="12" rx="1.5" fill="#00b5ef"/><path d="M4 2.5v6.6l1.6-1.5 1.2 2.5 1-.5-1.2-2.4h2.2z" fill="#fff"/></symbol>
    <symbol id="ic-pin-plain" viewBox="0 0 12 12"><path d="M6 1a3.5 3.5 0 0 0-3.5 3.5C2.5 7.2 6 11 6 11s3.5-3.8 3.5-6.5A3.5 3.5 0 0 0 6 1z" fill="#fff"/><circle cx="6" cy="4.5" r="1.3" fill="#0056a2"/></symbol>
  </defs>
</svg>

<main class="canvas">
  <section class="letterhead">
    <div class="brand"><span class="brand-dot"></span>TLR Property</div>

    <ul class="head-contact">
      <li class="addr"><span>2710 Harbor Crest Avenue<br>Portland, OR 97205</span><svg class="icon"><use href="#ic-pin"/></svg></li>
      <li>+00 987 654 32<svg class="icon"><use href="#ic-phone"/></svg></li>
      <li>hello@tlrproperty.example<svg class="icon"><use href="#ic-mail"/></svg></li>
      <li>www.tlrproperty.example<svg class="icon"><use href="#ic-web"/></svg></li>
    </ul>

    <div class="head-rule"></div>

    <div class="recipient">
      <h2>MARA LINDQVIST</h2>
      <p>0987-654-321</p>
      <p>mara@lindqvistmail.example</p>
      <p class="tight">5580 Meadow Park Rd. Suite</p>
      <p class="tight">410 Austin, TX 78701</p>
    </div>

    <div class="body-copy">
      <p>Lorem ipsum dolor sit amet, consectetuer adipiscing elit, sed diam nonummy nibh euismod tincidunt ut laoreet dolore magna aliquam erat volutpat. Ut wisi enim ad minim veniam, quis nostrud exerci tation ullamcorper suscipit lobortis nisl ut aliquip ex ea commodo consequat. Duis autem vel eum iriure dolor in hendrerit in vulputate velit esse molestie consequat, vel illum dolore eu feugiat nulla facilisis at vero eros et accumsan et iusto odio dignissim qui blandit praesent luptatum zzril delenit augue duis dolore te feugait nulla facilisi.</p>
      <p>Lorem ipsum dolor sit amet, cons ectetuer adipiscing elit, sed diam nonummy nibh euismod tincidunt ut laoreet dolore magna aliquam erat volutpat. Ut wisi enim ad minim veniam, quis nostrud exerci tation ullamcorper suscipit lobortis nisl ut aliquip ex ea commodo consequat.</p>
    </div>

    <div class="signature" role="img" aria-label="Handwritten signature of Mara Lindqvist"></div>
    <p class="signer">Mr. Mara Lindqvist</p>

    <div class="foot-band"><svg class="icon" style="width:9px;height:9px"><use href="#ic-pin-plain"/></svg>2710 Harbor Crest Avenue Portland, OR 97205</div>
  </section>

  <section class="card card-front">
    <h3>DANIEL R. <strong>HARTWELL</strong></h3>
    <p class="role">Managing Director</p>
    <div class="card-addr"><svg class="icon"><use href="#ic-pin"/></svg><span>2710 Harbor Crest Avenue<br>Portland, OR 97205</span></div>
    <ul class="card-band">
      <li><svg class="icon"><use href="#ic-phone"/></svg>+00 987 654 32</li>
      <li><svg class="icon"><use href="#ic-mail"/></svg>hello@tlrproperty.example</li>
      <li><svg class="icon"><use href="#ic-web"/></svg>www.tlrproperty.example</li>
    </ul>
  </section>

  <section class="card card-back">
    <div class="brand"><span class="brand-dot"></span>TLR Property</div>
  </section>
</main>
</body>
</html>
```